Card design for Heating and Cooling company

this is for a heating and cooling company we recently updated our logo and need to update our cards. We attached our logo so you can incorporate it into the card. We specialize in residential and commercial furnace and air condition repairs. Have been in business since 2014.

Phone number 555.284.9137

We need the following phrases
:Repairs, Installations, and maintenance
:Quality work at reasonable prices
:residential/commercial
:Licensed &Insured
:Email Pinegrovehvac47@mailbox-example.com
Name: Teodor K (Ted)
Also on back side I would like my logo with wording :Thank you for your business and refferal

Industry/Entity Type

Hvac

Contact Information for Business Card

:residential/commercial
:Licensed & Insured
Name: Teodor K (Ted)
Number:555.284.9136

Requirements
Must have
• Blue and red colors
Nice to have
• Maybe a pic of a furnace or air conditioner

```html
<!DOCTYPE html>
<html lang="en">
<head>
<meta charset="utf-8">
<title>Pinegrove Heating &amp; Cooling — Business Card</title>
<link href="https://fonts.googleapis.com/css2?family=Open+Sans:wght@400;600;700&display=swap" rel="stylesheet">
<style>
  :root {
    --page-bg: #e9e9eb;
    --card-white: #ffffff;
    --brand-orange: #f47b20;
    --band-dark: #111111;
    --band-mid: #5a5a5a;
    --ink: #1a1a1a;
    --ink-light: #ffffff;
    --brand-blue: #2f8fd8;
  }
  * { box-sizing: border-box; margin: 0; padding: 0; }
  html, body { width: 1200px; height: 900px; overflow: hidden; }
  body {
    background: var(--page-bg);
    font-family: "Open Sans", Arial, sans-serif;
    display: flex; flex-direction: column; align-items: center; justify-content: center;
    gap: 40px;
  }
  .card {
    width: 700px; height: 400px;
    background: var(--card-white);
    position: relative; overflow: hidden;
    box-shadow: 0 6px 18px rgba(0,0,0,.18);
  }
  .brand-name {
    display: flex; align-items: center; gap: 14px;
    font-weight: 700; color: var(--ink);
    text-transform: uppercase; letter-spacing: .5px; line-height: 1.15;
  }
  .brand-mark { width: 38px; height: 38px; border-radius: 50%; background: var(--brand-blue); flex: none; }
  .brand-name span { font-size: 26px; }
  .brand-name small { display: block; font-size: 13px; letter-spacing: 3px; }

  /* back side */
  .card--back .brand-name { position: absolute; top: 90px; left: 50%; transform: translateX(-50%); white-space: nowrap; }
  .thanks-band {
    position: absolute; left: 0; right: 0; top: 262px; height: 66px;
    background: linear-gradient(180deg, var(--band-dark) 0%, var(--band-mid) 50%, var(--band-dark) 100%);
    display: flex; align-items: center; justify-content: center;
    color: var(--ink-light); font-size: 18px; letter-spacing: .3px;
  }

  /* front side */
  .card--front { display: flex; }
  .front-brand { width: 44%; display: flex; align-items: center; justify-content: center; }
  .front-brand .brand-name span { font-size: 21px; }
  .front-brand .brand-name small { font-size: 11px; letter-spacing: 2px; }
  .front-details {
    width: 56%; background: var(--brand-orange); color: var(--ink-light);
    padding: 70px 36px 0 36px;
  }
  .person-name { font-size: 24px; font-weight: 700; }
  .person-title { font-size: 13px; margin-bottom: 16px; }
  .services { list-style: none; font-size: 15px; line-height: 1.55; margin-bottom: 18px; }
  .services li { display: flex; align-items: center; gap: 8px; }
  .contact { font-size: 15px; line-height: 1.6; }
  .contact div { display: flex; align-items: center; gap: 9px; }
  svg.icon { width: 16px; height: 16px; flex: none; }
</style>
</head>
<body>
  <section class="card card--back">
    <div class="brand-name">
      <i class="brand-mark"></i>
      <div><span>Pinegrove</span><small>Heating &amp; Cooling</small></div>
    </div>
    <div class="thanks-band">Thank you for your business and refferal</div>
  </section>

  <section class="card card--front">
    <div class="front-brand">
      <div class="brand-name">
        <i class="brand-mark"></i>
        <div><span>Pinegrove</span><small>Heating &amp; Cooling</small></div>
      </div>
    </div>
    <div class="front-details">
      <p class="person-name">Teodor K</p>
      <p class="person-title">President</p>
      <ul class="services">
        <li><svg class="icon" viewBox="0 0 16 16"><path d="M2 8.5l4 4 8-9" fill="none" stroke="#fff" stroke-width="2.4"/></svg>Repairs, Installations, and maintenance</li>
        <li><svg class="icon" viewBox="0 0 16 16"><path d="M2 8.5l4 4 8-9" fill="none" stroke="#fff" stroke-width="2.4"/></svg>Quality work at reasonable prices</li>
        <li><svg class="icon" viewBox="0 0 16 16"><path d="M2 8.5l4 4 8-9" fill="none" stroke="#fff" stroke-width="2.4"/></svg>residential/commercial</li>
        <li><svg class="icon" viewBox="0 0 16 16"><path d="M2 8.5l4 4 8-9" fill="none" stroke="#fff" stroke-width="2.4"/></svg>Licensed &amp;Insured</li>
      </ul>
      <div class="contact">
        <div><svg class="icon" viewBox="0 0 16 16"><path d="M1 5c0-2 3-3 7-3s7 1 7 3v1h-3V4.5H4V6H1z M3 7h10l1 7H2z" fill="#fff"/></svg>555.284.9137</div>
        <div><svg class="icon" viewBox="0 0 16 16"><rect x="1" y="3" width="14" height="10" fill="#fff"/><path d="M1 3l7 6 7-6" fill="none" stroke="#f47b20" stroke-width="1.5"/></svg>Pinegrovehvac47@mailbox-example.com</div>
      </div>
    </div>
  </section>
</body>
</html>
```